Design a logo and bottle label for Tarnwell Distillery Irish cream

We are Tarnwell Distillery and we want you to design a logo and bottle label for our new alcoholic Irish cream called Tarnwell Distillery Irish cream

We want a stylish simple label, Google marden vale creamery chocolate milk to get an understanding of what type of design we are looking for

You can look on our website "http://www.tarnwelldistillery-demo.com

There are 3 different bottle sizes, 250 ml, 500 ml and 750 ml details below:
http://www.velorvetro-demo.com/en_GB/prodotti/gourmet/showproduct/kav2/cal-vaso-750-r-58-ue

Files included in this contest:
Tarnwell Distillery Logo "Tarnwell Distillery - Logo 2 White black.ai"
Including on the back of the bottle it needs to have the same details as shown "back of bottle.jpg"

***********Only original work will be accepted for the final winner**********************

Final design needs to be 3D design and flatten design attached "bottle drawing.pdf"

If we find a good design will close the contest early so don't wait to long to get your designs in

We have over 30 brands which will need logos as well, so who ever wins this one will be invited back for them first

Guaranteed Contest and hopefully a higher standard of design

```html
<!DOCTYPE html>
<html lang="en">
<head>
<meta charset="utf-8">
<title>Tarnwell Distillery Irish Cream – Label</title>
<link rel="stylesheet" href="https://fonts.googleapis.com/css2?family=Questrial&family=Pinyon+Script&family=Arimo&display=swap">
<style>
  :root {
    --paper: #ffffff;
    --ink: #1f1f1f;
    --red: #e3141c;
    --tan: #d8b27a;
    --tan-dark: #b88f55;
    --shadow: #2a2a2a;
  }
  html, body {
    margin: 0;
    padding: 0;
    overflow: hidden;
    background: var(--paper);
  }
  .label {
    position: relative;
    width: 1200px;
    height: 1137px;
    background: var(--paper);
    overflow: hidden;
  }
  .mascot-art {
    position: absolute;
    left: 387px;
    top: 160px;
    width: 466px;
    height: 467px;
    border-radius: 46% 46% 40% 40%;
    background: radial-gradient(circle at 50% 55%, var(--tan) 0%, var(--tan-dark) 70%, #8a6a3c 100%);
  }
  .name-frame {
    position: absolute;
    left: 0;
    top: 0;
    width: 1200px;
    height: 1137px;
  }
  .frame-shadow { fill: var(--shadow); }
  .frame-body { fill: var(--paper); stroke: var(--ink); stroke-width: 3; }
  .brand-name {
    position: absolute;
    left: 0;
    width: 1200px;
    top: 650px;
    margin: 0;
    text-align: center;
    font-family: "Questrial", sans-serif;
    font-weight: 400;
    font-size: 62px;
    letter-spacing: 4px;
    color: var(--red);
    line-height: 1;
  }
  .brand-sub {
    position: absolute;
    left: 0;
    width: 1200px;
    top: 735px;
    text-align: center;
    font-family: "Questrial", sans-serif;
    font-size: 31px;
    letter-spacing: 3px;
    color: var(--ink);
    line-height: 1;
  }
  .product-name {
    position: absolute;
    left: 0;
    width: 1200px;
    top: 772px;
    text-align: center;
    font-family: "Pinyon Script", cursive;
    font-size: 98px;
    color: var(--red);
    line-height: 1.1;
  }
  .volume {
    position: absolute;
    left: 545px;
    top: 902px;
    font-family: "Arimo", sans-serif;
    font-size: 32px;
    color: var(--ink);
    line-height: 1;
  }
  .spirit-info {
    position: absolute;
    left: 790px;
    top: 1035px;
    width: 150px;
    text-align: center;
    font-family: "Arimo", sans-serif;
    font-size: 26px;
    color: var(--ink);
    line-height: 1.3;
  }
</style>
</head>
<body>
<main class="label">
  <div class="mascot-art" role="img" aria-label="Cartoon bull head mascot with horns and tongue out"></div>

  <svg class="name-frame" viewBox="0 0 1200 1137" aria-hidden="true">
    <g transform="translate(8 8)">
      <path class="frame-shadow" d="M 230 620 A 30 30 0 0 0 260 590 L 560 590 C 590 590 600 575 617 575 C 634 575 644 590 674 590 L 975 590 A 30 30 0 0 0 1005 620 L 1005 740 C 1005 760 1020 770 1020 780 C 1020 790 1005 800 1005 820 L 1005 940 A 30 30 0 0 0 975 970 L 674 970 C 644 970 634 985 617 985 C 600 985 590 970 560 970 L 260 970 A 30 30 0 0 0 230 940 L 230 820 C 230 800 215 790 215 780 C 215 770 230 760 230 740 Z"/>
    </g>
    <path class="frame-body" d="M 230 620 A 30 30 0 0 0 260 590 L 560 590 C 590 590 600 575 617 575 C 634 575 644 590 674 590 L 975 590 A 30 30 0 0 0 1005 620 L 1005 740 C 1005 760 1020 770 1020 780 C 1020 790 1005 800 1005 820 L 1005 940 A 30 30 0 0 0 975 970 L 674 970 C 644 970 634 985 617 985 C 600 985 590 970 560 970 L 260 970 A 30 30 0 0 0 230 940 L 230 820 C 230 800 215 790 215 780 C 215 770 230 760 230 740 Z"/>
  </svg>

  <h1 class="brand-name">TARNWELL</h1>
  <div class="brand-sub">DISTILLERY</div>
  <div class="product-name">Irish Cream</div>
  <div class="volume">750 ml</div>
  <div class="spirit-info">liqueur<br>17%Alc/vol.</div>
</main>
</body>
</html>
```